Brochure Design Project

We are a consulting engineering company and need to have our current company brochure updated and made to look a lot more professional.

We provide design and documentation of electrical, lighting, mechanical, hydraulic, fire, services to architects, interior designers, building owners and managers.

We are launching an updated website shortly and want a print brochure to send to clients.

Attached is our current brochure for reference.
Updates

The recent projects section should be renamed to "Completed Projects". Space should be allowed for 8 projects. I have uploaded 7 of these images and a new image will follow shortly.

We would like to include an image for each of our company services. I have uploaded 9 new images:

1. Electrical
2. Mechanical
3. Communications
4. Fire
5. Security
6. Lighting
7. Hydraulics
8. Computer Suite
9. Building Assessments

Target Market(s)

Architects, Interior Designers, Consultants, Professionals

Industry/Entity Type

Building

Requirements
Must have
• Very professional look
Simple and easy to read layout
Similar look and feel to our new website which is soon to be launched : http://www.loomtrail.co.uk/hvk/
Examples of our recent projects - around 6 projects with 1 or 2 photos per project. Will upload these soon.
A3 size, double sided with centre fold
Should not have
• Bright colours
Any comics or similar

```html
<!DOCTYPE html>
<html lang="en">
<head>
<meta charset="utf-8">
<title>Our Services – HVK Consulting Services</title>
<link href="https://fonts.googleapis.com/css2?family=Jost:wght@300;400&family=Roboto+Condensed:wght@300;400&display=swap" rel="stylesheet">
<style>
:root{
  --page-bg:#ffffff;
  --band-dark:#35312b;
  --head-light:#cfcfcf;
  --head-mid:#b4b4b4;
  --body-bg:#dadada;
  --ink:#2a2a2a;
  --ink-soft:#3c3c3c;
  --rule:#a9a9a9;
  --spine:#3a3631;
}
*{margin:0;padding:0;box-sizing:border-box}
html,body{width:1200px;height:900px;overflow:hidden;background:var(--page-bg)}
.spread{position:absolute;left:40px;top:55px;width:1120px;height:793px;background:var(--body-bg);overflow:hidden}
.top-band{position:absolute;left:0;top:0;width:100%;height:48px;background:var(--band-dark)}
.header-field{position:absolute;left:0;top:48px;width:100%;height:165px;
  background:radial-gradient(ellipse at 28% 55%,var(--head-light) 0%,var(--head-mid) 75%),var(--head-mid)}
.spine{position:absolute;left:558px;top:48px;width:2px;height:745px;background:var(--spine)}
.title{position:absolute;left:173px;top:94px;width:215px;border-top:2px solid #9c9c9c;border-bottom:2px solid #9c9c9c;
  font-family:"Jost",sans-serif;font-weight:300;font-size:27px;letter-spacing:4.6px;text-align:center;color:var(--ink);line-height:32px;padding-top:1px}
.intro{position:absolute;left:612px;top:97px;width:458px;font-family:"Roboto Condensed",sans-serif;font-weight:300;
  font-size:10.6px;line-height:13.6px;color:var(--ink)}
.intro .prompt{background:#222;color:#fff;padding:0 1px}
.service{position:absolute;font-family:"Roboto Condensed",sans-serif}
.service h2{font-family:"Jost",sans-serif;font-weight:400;font-size:12.5px;letter-spacing:1.9px;color:var(--ink);
  line-height:16px;margin-left:-24px;padding-left:24px;position:relative;white-space:nowrap}
.service h2 svg{position:absolute;left:0;top:0;width:16px;height:16px;fill:var(--ink)}
.service ul{list-style:none;margin-top:3px}
.service li{font-weight:300;font-size:10.6px;line-height:12.8px;color:var(--ink-soft);padding:1.6px 0 1.6px 8px;
  border-bottom:1px dotted var(--rule);position:relative}
.service li::before{content:"›";position:absolute;left:0;top:0.5px;font-size:13px}
.footer{position:absolute;top:762px;font-family:"Jost",sans-serif;font-size:6.5px;letter-spacing:1px;color:var(--ink-soft)}
.footer .num{font-size:9px;margin:0 5px}
.corner{position:absolute;top:760px;width:8px;height:10px;background:#222}
</style>
</head>
<body>
<div class="spread">
  <div class="top-band"></div>
  <div class="header-field"></div>
  <div class="spine"></div>

  <h1 class="title">OUR SERVICES</h1>
  <p class="intro"><span class="prompt">Please Provide the Short Discription about the Our Services:</span> Itatem volorem. Et et ilit, qui dolorpost aut fuga. Ficiur? Quassum nonseceseque conemol estrum que pore, ulluptat aut earunt labo. Eri num faceaquam a cor as nossuntur? incia cus reium ut ut assit que num qui re, quam, quiam que dolor aut moluptat. quae. Nemquibus volo ero et harions equamus apelit, con nonectendi dolorrum, non</p>

  <!-- Left page -->
  <section class="service" style="left:77px;top:229px;width:267px">
    <h2><svg viewBox="0 0 16 16"><path d="M8 1.5L15 14H1z" fill="none" stroke="#2a2a2a" stroke-width="1.4"/><path d="M7.3 6h1.4l-.3 4.5H7.6zM7.3 11.3h1.4v1.3H7.3z"/></svg>ELECTRICAL SERVICES</h2>
    <ul>
      <li>Power distribution</li><li>General lighting</li>
      <li>Feature lighting for highlight/contrast of client orientated areas</li>
      <li>Programmable lighting control</li><li>Emergency lighting and exit signs</li>
      <li>Electrical consumption management</li>
      <li>Lighting control integration with energy management systems</li>
      <li>Evacuation warning systems</li><li>Power conditioners</li>
      <li>Public address installations</li><li>Television signal distribution</li>
    </ul>
  </section>

  <section class="service" style="left:77px;top:458px;width:267px">
    <h2><svg viewBox="0 0 16 16"><path d="M8 1.5L15 14H1z" fill="none" stroke="#2a2a2a" stroke-width="1.4"/><path d="M7.3 6h1.4l-.3 4.5H7.6zM7.3 11.3h1.4v1.3H7.3z"/></svg>CRITICAL USE INSTALLATIONS</h2>
    <ul>
      <li>Layout and space allowance for hardware and equipment</li>
      <li>Uninterruptable power supplies and power conditioning</li>
      <li>Access control and intruder detection</li><li>Fire rating</li>
      <li>Anti static solutions</li><li>PABX and VOIP integration</li>
      <li>Dedicated electrical distribution systems</li><li>Stand-by power supplies</li>
      <li>High heat rejection cooling solutions</li>
    </ul>
  </section>

  <section class="service" style="left:77px;top:654px;width:259px">
    <h2><svg viewBox="0 0 16 16"><rect x="3" y="3" width="10" height="7" fill="none" stroke="#2a2a2a" stroke-width="1.5"/><path d="M1 11h14v2H1z"/></svg>COMPUTER SUITE AUDITS</h2>
    <ul>
      <li>Comprehensive Computer Suite Audits</li><li>Australian Standard Compliance</li>
      <li>TIA 942 Tier Rating certification</li>
    </ul>
  </section>

  <!-- Right page -->
  <section class="service" style="left:628px;top:229px;width:202px">
    <h2><svg viewBox="0 0 16 16"><rect x="1.5" y="1" width="4" height="12" rx="2" fill="none" stroke="#2a2a2a" stroke-width="1.3"/><rect x="8.5" y="1" width="4" height="12" rx="2" fill="none" stroke="#2a2a2a" stroke-width="1.3"/><rect x="3" y="7" width="1.2" height="6"/><rect x="10" y="5" width="1.2" height="8"/></svg>HYDRAULIC SERVICES</h2>
    <ul>
      <li>Water supplies</li><li>Waste discharge</li><li>Venting</li>
      <li>Water heating and cooling</li><li>Filtration</li>
    </ul>
  </section>

  <section class="service" style="left:868px;top:229px;width:199px">
    <h2><svg viewBox="0 0 16 16"><rect x="4" y="4" width="5" height="11" rx="1"/><path d="M4 2h7v1.5H4z"/><rect x="5.5" y="1" width="2" height="2"/></svg>FIRE SERVICES</h2>
    <ul>
      <li>Electronic Smoke and Thermal Detection</li><li>Aspirating Smoke Detection Systems</li>
      <li>Fire Suppression Systems</li><li>Fire Sprinkler Systems</li>
    </ul>
  </section>

  <section class="service" style="left:628px;top:362px;width:202px">
    <h2><svg viewBox="0 0 16 16"><path d="M2 3l10 10A7 7 0 0 1 2 3z"/><path d="M7 8l5-5" stroke="#2a2a2a" stroke-width="1.4"/><path d="M6 14h6v1.5H6z"/></svg>COMMUNICATION SYSTEMS</h2>
    <ul>
      <li>Telephone cabling</li><li>Data cabling</li><li>Patching philosophies</li>
      <li>Fibre optic distribution systems</li>
      <li>Integration of voice and data cabling systems</li><li>Hardware housings</li>
      <li>Compliance with relevant codes and installation practices</li>
      <li>LAN Cable distribution systems</li>
    </ul>
  </section>

  <section class="service" style="left:868px;top:362px;width:199px">
    <h2><svg viewBox="0 0 16 16"><path d="M2 14l7-7" stroke="#2a2a2a" stroke-width="2.4" stroke-linecap="round"/><path d="M9 2.5a3.5 3.5 0 1 0 4.5 4.5L11.5 7 9.5 5z"/></svg>MECHANICAL SERVICES</h2>
    <ul>
      <li>District Cooling System</li><li>Air and Water Cooled Chilled Water System</li>
      <li>BMS/BAS and DDC Control System</li><li>Computer and Data Centre Solutions</li>
      <li>DX-Type Water and Air Cooled System (Single or Multiple Indoor Units)</li>
      <li>VAV and Chilled Beams</li><li>Industrial and Commercial</li><li>Humidification</li>
      <li>Commercial and Industrial Evaporative Cooling Using Air Washers</li>
    </ul>
  </section>

  <section class="service" style="left:628px;top:588px;width:202px">
    <h2><svg viewBox="0 0 16 16"><path d="M4.5 7V5a3.5 3.5 0 0 1 7 0v2" fill="none" stroke="#2a2a2a" stroke-width="1.8"/><rect x="2.5" y="7" width="11" height="8" rx="1"/></svg>SECURITY SERVICES</h2>
    <ul>
      <li>Electronic access control</li>
      <li>Integration of existing systems with client requirements</li>
      <li>Intruder detection</li><li>Off site monitoring and alarms</li><li>CCTV</li>
    </ul>
  </section>

  <section class="service" style="left:868px;top:588px;width:199px">
    <h2><svg viewBox="0 0 16 16"><path d="M1 15V7h4V15zM6 15V2h5V15zM12 15V5h3V15z" fill="none" stroke="#2a2a2a" stroke-width="1.2"/><path d="M7.5 4h2v1.5h-2zM7.5 7h2v1.5h-2zM7.5 10h2v1.5h-2z"/></svg>BUILDING ASSESSMENT</h2>
    <ul>
      <li>Building services condition assessment</li>
      <li>Advise relative to available building services (for long or short term purpose)</li>
      <li>Trouble Shooting and Investigation</li><li>Review of Existing Systems</li>
      <li>Upgrade for Current and Future Refurbishment</li>
    </ul>
  </section>

  <div class="corner" style="left:0"></div>
  <div class="corner" style="right:0"></div>
  <p class="footer" style="left:48px"><span class="num">8</span>HVK CONSULTING SERVICES (PTY) LTD.</p>
  <p class="footer" style="right:48px">HVK CONSULTING SERVICES (PTY) LTD.<span class="num">9</span></p>
</div>
</body>
</html>
```